I have looking for nice Photo for my Business Cards , see below details I justed send.

Please see my Website Link , It should be up and running my late tonight or tomorrow morning.

http://www.plushgetawaysglobal.example

Travel & Toursim

Company Name: Opaline Escapes Global

If you look at my Website it will show you photos that keep changing at the top. I want something like that or if you have some samples to show me.
Looking for a beach with sand and maybe having somebody resting on the beach with a drink or reading.

Let me know what you think.

Also what will be the cost hopefully you already got some photos to show me. I want my business Card to be glossy.

Industry/Entity Type

Business

Contact Information for Business Card

Contact: Rosalind Vettor
Mobile: 0431 297 654
Email: rosalind@opalineescapesweb.example
Website: www.plushgetawaysglobal.example

Requirements
Must have
• Company Name: Opaline Escapes Global
Contact: Rosalind Vettor
Mobile: 0431 297 654

```html
<!DOCTYPE html>
<html lang="en">
<head>
<meta charset="utf-8">
<title>Opaline Escapes Global – Business Card</title>
<link href="https://fonts.googleapis.com/css2?family=Lato:ital,wght@0,400;0,700;0,900;1,700;1,900&display=swap" rel="stylesheet">
<style>
  :root {
    --page-bg: #d9d3c8;
    --card-white: #ffffff;
    --accent-red: #e3131b;
    --ink: #1e1e1e;
    --sky-top: #1f5fc4;
    --sky-mid: #7fb2e6;
    --pool: #19b6d4;
    --pool-deep: #0b8fb8;
    --bullet: #2f8fd8;
    --bullet-light: #9fd3f7;
  }
  * { box-sizing: border-box; margin: 0; padding: 0; }
  html, body { width: 1200px; height: 1000px; overflow: hidden; }
  body {
    background: var(--page-bg);
    font-family: "Lato", Arial, sans-serif;
    position: relative;
  }
  .card {
    position: absolute;
    width: 620px;
    height: 410px;
    background: var(--card-white);
    overflow: hidden;
    box-shadow: 0 6px 18px rgba(0,0,0,0.18);
  }
  .card--front { left: 40px; top: 60px; }
  .card--back { left: 540px; top: 530px; }

  .front__scene { position: absolute; inset: 0; width: 100%; height: 100%; }

  .front__headline {
    position: absolute; right: 28px; top: 22px;
    text-align: right;
    color: var(--accent-red);
    font-weight: 900; font-style: italic;
    font-size: 21px; line-height: 1.1;
    letter-spacing: 2px;
  }
  .front__contact {
    position: absolute; right: 28px; top: 100px;
    text-align: right; color: var(--accent-red);
  }
  .front__name { font-size: 34px; font-weight: 900; line-height: 1.1; }
  .front__phone { font-size: 24px; font-weight: 900; line-height: 1.1; margin-top: 4px; }
  .front__region { font-size: 15px; font-weight: 400; line-height: 1.1; }

  .front__online {
    position: absolute; right: 28px; bottom: 24px;
    text-align: right; color: var(--card-white);
    font-weight: 700;
  }
  .front__email { font-size: 14px; display: flex; align-items: center; justify-content: flex-end; gap: 6px; white-space: nowrap; }
  .front__web { font-size: 17px; margin-top: 6px; white-space: nowrap; }
  .front__handle { font-size: 17px; margin-top: 6px; display: flex; align-items: center; justify-content: flex-end; gap: 6px; }
  .handle-dot { width: 16px; height: 16px; border-radius: 50%; background: var(--card-white); display: inline-block; }

  .company-mark {
    position: absolute; left: 60px; top: 800px;
    color: var(--card-white);
    font-weight: 400;
    font-size: 40px; line-height: 1.15;
    letter-spacing: 1px;
  }

  .back__columns {
    position: absolute; inset: 36px 30px 30px 40px;
    display: grid; grid-template-columns: 1fr 1fr; column-gap: 40px;
  }
  .benefits { list-style: none; }
  .benefit {
    position: relative; padding-left: 16px;
    font-size: 11.5px; font-weight: 700; color: var(--ink);
    line-height: 1.2; margin-bottom: 12px;
  }
  .benefit::before {
    content: ""; position: absolute; left: 0; top: 1px;
    width: 10px; height: 10px; border-radius: 50%;
    background: radial-gradient(circle at 35% 35%, var(--bullet-light), var(--bullet));
  }
  .benefits--right { padding-top: 14px; }
  .benefit--closing { margin-top: 12px; }
</style>
</head>
<body>

  <section class="card card--front" aria-label="Business card front">
    <svg class="front__scene" viewBox="0 0 620 410" preserveAspectRatio="none">
      <defs>
        <linearGradient id="sceneTones" x1="0" y1="0" x2="0" y2="1">
          <stop offset="0" stop-color="var(--sky-top)"/>
          <stop offset="0.45" stop-color="var(--sky-mid)"/>
          <stop offset="0.6" stop-color="var(--pool)"/>
          <stop offset="1" stop-color="var(--pool-deep)"/>
        </linearGradient>
        <linearGradient id="whiteFade" x1="1" y1="0" x2="0" y2="1">
          <stop offset="0.55" stop-color="#ffffff" stop-opacity="1"/>
          <stop offset="1" stop-color="#ffffff" stop-opacity="0"/>
        </linearGradient>
      </defs>
      <rect class="scene-photo" width="620" height="410" fill="url(#sceneTones)" role="img" aria-label="Photo of a clifftop infinity pool overlooking the sea, with a canopy daybed, a couple relaxing and pink flowers in the foreground"/>
      <path class="text-panel" d="M220 0 H620 V280 C500 270 360 170 220 0 Z" fill="url(#whiteFade)"/>
      <path class="text-panel-solid" d="M300 0 H620 V255 C520 240 400 150 300 0 Z" fill="#ffffff"/>
    </svg>

    <div class="front__headline">Luxury Worldwide Vacation<br>Do You LOVE to Travel?</div>

    <div class="front__contact">
      <div class="front__name">Rosalind Vettor</div>
      <div class="front__phone">0431 297 654</div>
      <div class="front__region">( Australia)</div>
      <div class="front__phone">+61 431 297 654</div>
      <div class="front__region">( International)</div>
    </div>

    <div class="front__online">
      <div class="front__email">
        <svg width="14" height="10" viewBox="0 0 14 10" aria-hidden="true"><rect x="0.5" y="0.5" width="13" height="9" fill="#fff"/><path d="M1 1 L7 6 L13 1" stroke="#0b8fb8" fill="none" stroke-width="1.2"/></svg>
        rosalind@opalineescapesweb.example
      </div>
      <div class="front__web">www.plushgetawaysglobal.example</div>
      <div class="front__handle"><span class="handle-dot"></span>rosalindvettor</div>
    </div>
  </section>

  <div class="company-mark">Opaline<br>Escapes Global</div>

  <section class="card card--back" aria-label="Business card back">
    <div class="back__columns">
      <ul class="benefits benefits--left">
        <li class="benefit">Select from thousands of worldwide hotels, resorts, condos and villas at huge savings.</li>
        <li class="benefit">Enjoy cruising with the world's best cruise lines to exotic ports at discounted prices..</li>
        <li class="benefit">Bonus weeks and half price specials around the world</li>
        <li class="benefit">Up to 80% savings on thousands of worldwide resorts &amp; holiday apartments</li>
        <li class="benefit">Up to 75% savings on major brand name hotel chains around the world</li>
        <li class="benefit">Up to 35% savings on 4, 5 and 6 star international cruise lines</li>
        <li class="benefit">Up to 70% savings on car rentals in thousands of worldwide locations</li>
        <li class="benefit">110% price guarantee on accommodation, cruises, car rentals, group tours, etc</li>
      </ul>
      <ul class="benefits benefits--right">
        <li class="benefit">Reward Points Program so you can book travel with rewards credits</li>
        <li class="benefit">Guest passes to give to friends or family as special occasion gifts</li>
        <li class="benefit">List your holiday home or exchange your timeshare for travel anywhere</li>
        <li class="benefit">Qualified travel experts to book your travel for you no additional cost</li>
        <li class="benefit">Take a guided tour with the best tour guides in the industry and enjoy huge savings.</li>
        <li class="benefit">Travel insurance at $79 per year for the whole family</li>
        <li class="benefit">Shopping discounts on over 250,000 products</li>
        <li class="benefit benefit--closing">and so much more we can't list it all here!</li>
      </ul>
    </div>
  </section>

</body>
</html>
```